Vinto PR Website

Vinto PR are a PR company with a requirement for a new website. In consultation with the client, we have defined a wireframe for a homepage to show content and functionality. A PDF of the wire frame is attached.
Current site http://www.vinto-pr.co.uk/
Updates
If you are using Stock Photography - please use PixVault
Dear All
Unfortunately, my client didn't like any of the designs submitted.
I've uploaded 3 examples of the type of photography that will appear in the carousel as supplied by the client.
Target Market(s)
Business to Business/Professionals - high value clients
Number of Pages Required
1 page
Requirements
Must have
- Colour scheme is attached as a .ase file from Kuler and can be viewed on Kuler if you search for 'VINTO PR Palette'
Corporate Typeface is Futura Book - use of Cufon is OK
Current Logo to be reatainedCall 2 Action Buttons will be controlled via the CMS so a generic background may be useful for these.
Nice to have
- RSS feeds

```html
<!DOCTYPE html>
<html lang="en">
<head>
<meta charset="utf-8">
<title>Vinto PR — Home</title>
<link rel="stylesheet" href="https://fonts.googleapis.com/css2?family=Oswald:wght@400;500&family=PT+Sans+Narrow&family=Tinos:wght@400;700&family=Montserrat:wght@600;700&family=Open+Sans:wght@400;600&family=Arimo&display=swap">
<style>
:root{
  --sky:#99ccff;
  --forest:#44674f;
  --forest-dark:#2f4a39;
  --aqua:#2fbbd8;
  --teal:#6ecbd3;
  --mint:#8ecfc0;
  --ink:#111;
  --white:#fff;
  --blue:#1d7fd1;
}
*{box-sizing:border-box;margin:0;padding:0}
html,body{width:1200px;height:2373px;overflow:hidden}
body{background:var(--sky);position:relative;font-family:'Open Sans',sans-serif;color:var(--ink)}
.page{position:absolute;left:61px;top:0;width:1080px;height:2373px;background:var(--white)}
.abs{position:absolute}
/* header */
.hero{left:0;top:0;width:1080px;height:441px;background:linear-gradient(180deg,#9fa3a8 0%,#8c8f86 40%,#6f7a55 70%,#dcdde3 100%)}
.logo{left:20px;top:14px;font-family:'Open Sans',sans-serif;font-size:42px;font-weight:400;letter-spacing:14px;color:#111}
.top-tabs{left:508px;top:11px;display:flex;gap:12px}
.top-tab{width:123px;height:53px;background:linear-gradient(180deg,#a9e6ea,#57c2cc);border:2px solid #7fd0d6;border-radius:4px 4px 0 0;box-shadow:4px 4px 6px rgba(0,0,0,.35);font-family:'Oswald',sans-serif;font-size:22px;color:#123;text-align:center;line-height:30px}
.hero-title{left:0;width:1080px;top:138px;text-align:center;font-family:'Oswald',sans-serif;font-weight:500;font-size:46px;color:var(--blue);text-shadow:2px 2px 0 #06223a}
.callus{right:32px;top:398px;font-family:'Oswald',sans-serif;font-weight:500;font-size:28px;color:#111;display:flex;align-items:center;gap:6px}
/* nav */
.nav{left:0;top:444px;width:1080px;height:100px;background:var(--forest);border:3px solid var(--forest-dark);display:flex;align-items:center;justify-content:center;font-family:'Oswald',sans-serif;font-size:29px;color:var(--aqua)}
.nav span.sep{color:var(--white);margin:0 3px}
/* services panel */
.services{left:0;top:550px;width:1080px;height:385px;background:var(--teal);border:2px solid #3a9aa6;border-radius:18px}
.svc-btn{left:25px;width:305px;height:48px;background:linear-gradient(180deg,#fff,#d7dbe0);border-radius:24px;box-shadow:0 3px 5px rgba(0,0,0,.35);font-family:'Montserrat',sans-serif;font-weight:700;font-size:17px;display:flex;align-items:center;justify-content:center;padding-right:44px}
.svc-btn svg{position:absolute;right:4px;top:2px}
.scroll-text{left:348px;top:3px;width:680px;height:372px;background:var(--white);overflow:hidden;font-family:'Tinos',serif;font-size:18.5px;line-height:26.5px;padding-left:2px}
.scroll-text h2{font-size:30px;margin:26px 0 22px;font-weight:700}
.scrollbar{left:1026px;top:3px;width:20px;height:372px;background:#f2f2f2;border-left:1px solid #ddd}
.scrollbar .thumb{position:absolute;left:3px;top:98px;width:14px;height:54px;background:#fafafa;border:1px solid #bbb;border-radius:2px}
/* intro */
.intro-title{left:27px;top:940px;font-family:'Open Sans',sans-serif;font-size:48px;font-weight:400}
.intro-text{left:27px;top:1008px;width:650px;font-family:'PT Sans Narrow',sans-serif;font-size:21px;line-height:30.5px;color:#222}
.side-col{left:696px;top:960px;width:381px;height:714px;background:var(--mint)}
.case-photo{left:11px;top:11px;width:360px;height:400px;background:linear-gradient(180deg,#6a6e75,#3d4450 55%,#8f95a8);display:flex;justify-content:center;padding-top:110px;font-family:'Oswald',sans-serif;font-size:29px;color:var(--blue);text-align:center;line-height:40px}
.cta-shield{left:45px;top:424px}
.cta-text{left:45px;top:450px;width:283px;text-align:center;font-family:'Oswald',sans-serif;font-weight:500;font-size:40px;line-height:57px;color:#111}
.cta-text .accent{color:var(--blue)}
.news{left:0;top:1293px;width:337px;height:384px;border:2px solid #5f9a86}
.news h3{position:absolute;left:64px;top:8px;font-family:'Open Sans',sans-serif;font-weight:400;font-size:18px;width:243px;border-bottom:2px solid #5f9a86;padding-bottom:6px}
.news p{position:absolute;left:54px;top:62px;width:270px;font-family:'Arimo',sans-serif;font-size:22px;line-height:29px;text-align:justify}
.consumer-photo{left:348px;top:1293px;width:336px;height:384px;background:linear-gradient(180deg,#8a8f96,#6d5f58 55%,#c9c9cc);display:flex;align-items:flex-end;justify-content:center;padding-bottom:14px;font-family:'Oswald',sans-serif;font-size:30px;color:var(--blue);text-shadow:1px 1px 0 #06223a}
/* blog */
.blog{left:0;top:1691px;width:1080px;height:283px;border:3px solid var(--forest)}
.blog h3{position:absolute;left:63px;top:18px;width:285px;border-bottom:2px solid #444;padding-bottom:6px;font-family:'Open Sans',sans-serif;font-weight:600;font-size:30px}
.blog p{position:absolute;left:50px;top:90px;width:650px;font-family:'PT Sans Narrow',sans-serif;font-weight:700;font-size:23px;line-height:30px}
.blog .thumb{position:absolute;left:794px;top:23px;width:117px;height:124px;background:#000}
/* footer */
.footer{left:0;top:1981px;width:1080px;height:276px;background:var(--forest)}
.foot-col{top:30px;font-family:'Montserrat',sans-serif;font-weight:600;font-size:18px;line-height:31px;color:var(--aqua);list-style:none}
.signup-label{left:797px;top:9px;font-family:'Montserrat',sans-serif;font-weight:600;font-size:18px;color:var(--aqua)}
.email-box{left:776px;top:39px;width:204px;height:30px;background:var(--white);border:1px solid #999;font-family:'Arimo',sans-serif;font-size:18px;padding:2px 4px}
.subscribe{left:776px;top:98px;width:203px;height:44px;border-radius:22px;background:linear-gradient(180deg,#7a8d90,#3f5256);border:2px solid #cfe;font-family:'Montserrat',sans-serif;font-weight:700;font-size:21px;color:var(--white);text-align:center;line-height:40px}
.legal{left:0;top:2257px;width:1080px;height:70px;background:#000;color:var(--white);font-family:'Open Sans',sans-serif;font-size:18px;text-align:right;padding:18px 14px 0 0}
</style>
</head>
<body>
<div class="page">
  <header class="abs hero" role="img" aria-label="Photo of people dining outdoors above a city skyline">
    <div class="abs logo">Vinto PR</div>
    <nav class="abs top-tabs">
      <div class="top-tab">Email Us</div>
      <div class="top-tab">Voxly</div>
      <div class="top-tab">Chirper</div>
      <div class="top-tab">Facepage</div>
    </nav>
    <div class="abs hero-title">Real People</div>
    <div class="abs callus">Call us now
      <svg width="16" height="36" viewBox="0 0 16 36"><rect x="1" y="6" width="14" height="29" rx="3" fill="#111"/><rect x="3" y="0" width="3" height="8" fill="#111"/><rect x="4" y="10" width="8" height="8" fill="#f5a623"/></svg>
      0161 555 0199</div>
  </header>

  <nav class="abs nav">
    Home<span class="sep">|</span>Real Services<span class="sep">|</span>Press Office<span class="sep">|</span>Real Case Studies<span class="sep">|</span>Real People<span class="sep">|</span>Blog<span class="sep">|</span>Real News<span class="sep">|</span>Contact Us
  </nav>

  <section class="abs services">
    <div class="abs svc-btn" style="top:13px">Online public Relation<svg width="44" height="44"><circle cx="22" cy="22" r="19" fill="#3d8fd6" stroke="#bcd" stroke-width="3"/><path d="M16 13 L31 22 L16 31Z" fill="#0b2a4a"/></svg></div>
    <div class="abs svc-btn" style="top:90px">Media Relations<svg width="44" height="44"><circle cx="22" cy="22" r="19" fill="#3d8fd6" stroke="#bcd" stroke-width="3"/><path d="M16 13 L31 22 L16 31Z" fill="#0b2a4a"/></svg></div>
    <div class="abs svc-btn" style="top:165px">Consumer Campaigns<svg width="44" height="44"><circle cx="22" cy="22" r="19" fill="#3d8fd6" stroke="#bcd" stroke-width="3"/><path d="M16 13 L31 22 L16 31Z" fill="#0b2a4a"/></svg></div>
    <div class="abs svc-btn" style="top:238px">Crisis Public Relations<svg width="44" height="44"><circle cx="22" cy="22" r="19" fill="#3d8fd6" stroke="#bcd" stroke-width="3"/><path d="M16 13 L31 22 L16 31Z" fill="#0b2a4a"/></svg></div>
    <div class="abs svc-btn" style="top:312px;padding-right:40px;font-size:16.5px">Internal Communications<svg width="44" height="44"><circle cx="22" cy="22" r="19" fill="#3d8fd6" stroke="#bcd" stroke-width="3"/><path d="M16 13 L31 22 L16 31Z" fill="#0b2a4a"/></svg></div>
    <div class="abs scroll-text">
      <p>dictum sed pulvinar ligula viverra. Nam diam sem, faucibus semper placerat commodo, hendrerit at turpis. Phasellus sapien ipsum, interdum ut dapibus in, hendrerit nec nulla. Donec egestas scelerisque metus, nec placerat lectus ultrices ac. Nam sodales mollis euismod. Mauris ornare viverra dignissim. Phasellus sapien ipsum, interdum ut dapibus in, hendrerit nec nulla. Donec egestas scelerisque metus, nec placerat lectus ultrices ac. Nam sodales mollis euismod. Mauris ornare viverra dignissim.</p>
      <h2>Media Relation</h2>
      <p>Proin a ipsum et nisl luctus varius quis mattis dui. Mauris euismod enim eu enim scelerisque vitae lobortis quam aliquet. Praesent vestibulum lorem eu elit lobortis ac cursus odio mollis. Fusce magna magna, vestibulum eget fermentum at, blandit ut risus. Praesent blandit justo vel eros dictum sed.</p>
    </div>
    <div class="abs scrollbar"><div class="thumb"></div></div>
  </section>

  <h1 class="abs intro-title">Introduction</h1>
  <p class="abs intro-text">Lorem ipsum dolor sit amet, consectetur adipiscing elit. Proin a ipsum et nisl luctus varius quis mattis dui. Mauris euismod enim eu enim scelerisque vitae lobortis quam aliquet. Praesent vestibulum lorem eu elit lobortis ac cursus odio mollis. Fusce magna magna, vestibulum eget fermentum at, blandit ut risus. Praesent blandit justo vel eros dictum sed pulvinar ligula viverra. Nam diam sem, faucibus semper placerat commodo, hendrerit at turpis. Phasellus sapien ipsum, interdum ut dapibus in, hendrerit nec nulla. Donec egestas scelerisque metus, nec placerat lectus ultrices ac. Nam sodales mollis euismod. Mauris ornare viverra dignissim.</p>

  <aside class="abs side-col">
    <div class="abs case-photo" role="img" aria-label="Photo of a team serving dishes at an outdoor table">Real Case<br>Studies</div>
    <svg class="abs cta-shield" width="290" height="250" viewBox="0 0 290 250">
      <path d="M5 235 L45 210 L245 210 L285 235 L145 250Z" fill="#57bfd0"/>
      <path d="M10 2 L280 2 L278 210 Q145 260 12 210Z" fill="#3fbcd8" stroke="#2a8fb0" stroke-width="2"/>
    </svg>
    <div class="abs cta-text">To know the<br><span class="accent">Real Services</span><br>Please click here</div>
  </aside>

  <section class="abs news">
    <h3>Clients News</h3>
    <p>Phasellus sapien ipsum, interdum ut dapibus in, hendrerit nec nulla. Donec egestas scelerisque etus, nec placerat lectus ultrices ac. Nam sodales mollis euismod. Mauris ornare viverra dignissim.</p>
  </section>
  <div class="abs consumer-photo" role="img" aria-label="Photo of shoppers on a busy street beside a promotional stand">Consumer Campaigns</div>

  <section class="abs blog">
    <h3>Blog Entries</h3>
    <p>Phasellus sapien ipsum, interdum ut dapibus in, hendrerit nec nulla. Donec egestas scelerisque metus, nec placerat lectus ultrices ac. Nam sodales mollis euismod. Mauris ornare viverra dignissim.</p>
    <div class="thumb"></div>
  </section>

  <footer class="abs footer">
    <ul class="abs foot-col" style="left:55px">
      <li>Online Public Relations</li><li>Media Relations</li><li>Consumer Campaigns</li><li>Crisis Public Relations</li><li>Internal Communications</li>
    </ul>
    <ul class="abs foot-col" style="left:412px">
      <li>Subscribe to RSS Feed</li><li>Our Facepage page</li><li>Link Three</li><li>Link Four</li>
    </ul>
    <div class="abs signup-label">Enews Sign-up</div>
    <div class="abs email-box">Email Address</div>
    <div class="abs subscribe">Subscribe</div>
  </footer>
  <div class="abs legal">© Copyright Notice | Site Credit | Legal</div>
</div>
</body>
</html>
```